The Wrenfield Hotel Flyer

it is for a Pub that has been in the area for a long time but now we have changed the name and taken over as new owners and now have to try to get all the locals back, eating and drinking..

This Flyer is to try get all the locals to come try the new Wrenfield Hotel.

We have a great new menu with daily food deals
Craft beers
Week nights Live music
Tuesday Comedy night
Sunday live music

Industry/Entity Type

Hotel

```html
<!DOCTYPE html>
<html lang="en">
<head>
<meta charset="utf-8">
<title>The Wrenfield Hotel – Flyer</title>
<link rel="stylesheet" href="https://fonts.googleapis.com/css2?family=Montserrat:wght@300;400;800&family=Playfair+Display:wght@900&display=swap">
<style>
  :root {
    --navy: #262f6b;
    --teal: #4bbccb;
    --rust: #b9602b;
    --paper: #f4f2ea;
  }
  * { margin: 0; padding: 0; box-sizing: border-box; }
  html, body { width: 1200px; height: 2517px; overflow: hidden; background: var(--paper); }
  .flyer {
    position: relative;
    width: 1200px;
    height: 2517px;
    background: var(--paper);
    font-family: "Montserrat", sans-serif;
    color: var(--navy);
  }
  .flyer__art { position: absolute; inset: 0; }
  .line { position: absolute; left: 0; width: 100%; text-align: center; line-height: 1; white-space: nowrap; }

  .brand { font-weight: 800; color: var(--navy); }
  .brand--small { font-size: 58px; letter-spacing: 10px; }
  .brand--name { font-size: 138px; letter-spacing: 4px; }

  .headline { font-weight: 800; font-size: 108px; letter-spacing: 1px; z-index: 2; }
  .ampersand {
    font-family: "Playfair Display", serif;
    font-weight: 900;
    font-size: 470px;
    color: var(--rust);
    z-index: 1;
  }

  .event__day { font-weight: 300; font-size: 112px; letter-spacing: 1px; }
  .event__what { font-weight: 800; font-size: 110px; letter-spacing: 1px; }

  .web { font-weight: 800; font-size: 29px; letter-spacing: 0.5px; }
</style>
</head>
<body>
<main class="flyer">
  <svg class="flyer__art" width="1200" height="2517" viewBox="0 0 1200 2517" aria-hidden="true">
    <!-- frame -->
    <rect x="34" y="34" width="1132" height="2450" fill="none" stroke="var(--navy)" stroke-width="3"/>
    <g fill="none" stroke="var(--navy)" stroke-width="4">
      <polyline points="63,126 63,63 126,63"/>
      <polyline points="1074,63 1137,63 1137,126"/>
      <polyline points="63,2392 63,2455 126,2455"/>
      <polyline points="1074,2455 1137,2455 1137,2392"/>
    </g>
    <!-- top rule -->
    <line x1="380" y1="147" x2="820" y2="147" stroke="var(--rust)" stroke-width="4"/>
    <circle cx="600" cy="147" r="27" fill="var(--teal)"/>
    <!-- chevrons -->
    <g fill="var(--teal)">
      <polygon points="535,650 600,700 665,650 665,672 600,722 535,672"/>
      <polygon points="535,710 600,760 665,710 665,732 600,782 535,732"/>
    </g>
    <!-- divider -->
    <line x1="73" y1="1433" x2="1133" y2="1433" stroke="var(--teal)" stroke-width="3"/>
    <circle cx="600" cy="1433" r="62" fill="var(--paper)" stroke="var(--rust)" stroke-width="4"/>
    <circle cx="600" cy="1433" r="36" fill="var(--rust)"/>
  </svg>

  <!-- flourish ends -->
  <div role="img" aria-label="Small rust scroll flourish" style="position:absolute;left:294px;top:134px;width:86px;height:26px;background:var(--rust);opacity:.75;border-radius:13px"></div>
  <div role="img" aria-label="Small rust scroll flourish" style="position:absolute;left:820px;top:134px;width:86px;height:26px;background:var(--rust);opacity:.75;border-radius:13px"></div>
  <div role="img" aria-label="Teal filigree ornament" style="position:absolute;left:73px;top:1400px;width:210px;height:66px;background:var(--teal);opacity:.55;border-radius:33px"></div>
  <div role="img" aria-label="Teal filigree ornament" style="position:absolute;left:917px;top:1400px;width:216px;height:66px;background:var(--teal);opacity:.55;border-radius:33px"></div>

  <header class="masthead">
    <div class="line brand brand--small" style="top:264px">THE</div>
    <div class="line brand brand--name" style="top:356px">WRENFIELD</div>
    <div class="line brand brand--small" style="top:522px">HOTEL</div>
  </header>

  <section class="offers">
    <div class="line headline" style="top:812px">DAILY FOOD</div>
    <div class="line headline" style="top:923px">DEALS</div>
    <div class="line ampersand" style="top:830px">&amp;</div>
    <div class="line headline" style="top:1210px">CRAFT BEERS</div>
  </section>

  <section class="events">
    <div class="line event__day" style="top:1566px">WEEK NIGHTS</div>
    <div class="line event__what" style="top:1671px">LIVE MUSIC</div>
    <div class="line event__day" style="top:1818px">TUESDAY</div>
    <div class="line event__what" style="top:1923px">COMEDY NIGHT</div>
    <div class="line event__day" style="top:2070px">SUNDAY</div>
    <div class="line event__what" style="top:2175px">LIVE MUSIC</div>
  </section>

  <footer class="line web" style="top:2400px">www.wrenfieldhotel.com</footer>
</main>
</body>
</html>
```